Pause Your Day And Browse- PYDB poster

I am the Vice President of Advocacy for the Coastline Shelfkeepers Guild. I am looking to have a set of posters made for PYDB (Pause Your Day and Browse) October 23. PYDB is a time when all school children in BC are encouraged to Pause Your Day and Browse for 15-20 minutes at some point in their day.

I would like to get a set of 2 digital posters designed (if possible it would be nice to have the option to print to both 11 x 17 and 8.5 x 11 paper). We need a poster that is high school (Grade 8-12) appropriate and one that is elementary (Grade k-7) appropriate. Both posters need to be replicated in French. All posters need to have the KWNU logo on them as well as the Coastline Shelfkeepers Guild Logo.

Here is a link to last year's successful design http://kwnu-example.org/csg/info/advocacy.html
There are two additional samples in the uploaded files section.

Each poster needs to have the following information:

-Pause Your Day and Browse (PYDB)
- The date Monday, October 23, 2017
-the logo for the KWNU (attached)
-the logo for the CSG (attached)- the logos do not have to be large.

Target Market(s)

Children ages 5-12 and 12-17 as well as their teachers

Industry/Entity Type

Teacher

Font styles to use
Sans Serif

Requirements
Must have
• Must have both logos- colours may be changed for either or both
Nice to have
• Clear, Bright lettering. Images of child or children enjoying reading
Should not have
• stereotypes

```html
<!DOCTYPE html>
<html lang="en">
<head>
<meta charset="utf-8">
<title>PYDB – Pause Your Day And Browse</title>
<link href="https://fonts.googleapis.com/css2?family=Roboto+Condensed:wght@700&display=swap" rel="stylesheet">
<style>
  :root {
    --salmon: #e47a66;
    --peach: #eea293;
    --blush: #f6cbc3;
    --white: #ffffff;
    --band: #e97b67;
    --leaf-light: #9cc27f;
    --leaf: #5f8f48;
    --leaf-dark: #2f4a26;
    --bark: #3e2a1e;
    --bark-dark: #1c130d;
  }
  html, body {
    margin: 0;
    padding: 0;
    width: 1200px;
    height: 927px;
    overflow: hidden;
    background: #ffffff;
  }
  .poster {
    position: relative;
    width: 1200px;
    height: 927px;
    overflow: hidden;
    font-family: "Roboto Condensed", "Arial Narrow", sans-serif;
    font-weight: 700;
  }
  .scene-photo {
    position: absolute;
    inset: 0;
    background:
      radial-gradient(ellipse 520px 380px at 760px 200px, var(--leaf-light) 0%, rgba(156,194,127,0) 100%),
      linear-gradient(160deg, rgba(0,0,0,0) 45%, rgba(62,42,30,0.85) 62%, var(--bark) 78%, var(--bark-dark) 100%),
      linear-gradient(90deg, var(--leaf-dark) 0%, var(--leaf) 40%, var(--leaf) 75%, var(--leaf-dark) 100%);
  }
  .headline {
    position: absolute;
    left: 42px;
    top: 196px;
    margin: 0;
    font-size: 232px;
    line-height: 1;
    letter-spacing: 1px;
    text-transform: uppercase;
  }
  .headline span:nth-child(1) { color: var(--salmon); }
  .headline span:nth-child(2) { color: var(--peach); }
  .headline span:nth-child(3) { color: var(--blush); }
  .headline span:nth-child(4) { color: var(--white); }
  .tagline {
    position: absolute;
    left: 44px;
    margin: 0;
    text-transform: uppercase;
    line-height: 1;
  }
  .tagline-top {
    top: 428px;
    font-size: 66px;
    color: var(--salmon);
  }
  .tagline-bottom {
    top: 498px;
    font-size: 104px;
    color: var(--white);
  }
  .tagline-bottom .soft { color: var(--blush); }
  .date-band {
    position: absolute;
    left: 0;
    top: 640px;
    width: 600px;
    height: 66px;
    background: var(--band);
    border-radius: 0 6px 6px 0;
    color: var(--white);
    font-size: 46px;
    line-height: 66px;
    padding-left: 42px;
    box-sizing: border-box;
  }
  .partner {
    position: absolute;
    display: flex;
    align-items: center;
    gap: 10px;
    color: var(--white);
  }
  .partner-guild { left: 43px; top: 778px; }
  .partner-guild .mark {
    width: 92px;
    height: 92px;
    background: var(--white);
  }
  .partner-guild .name { font-size: 40px; }
  .partner-union { left: 242px; top: 798px; }
  .partner-union .mark {
    width: 46px;
    height: 46px;
    border-radius: 50%;
    background: var(--white);
  }
  .partner-union .name { font-size: 52px; }
</style>
</head>
<body>
<main class="poster">
  <div class="scene-photo" role="img" aria-label="Photo of a child sitting barefoot on a large tree branch in a green forest, reading a book beside a tied stack of books"></div>

  <h1 class="headline" aria-label="PYDB"><span>P</span><span>Y</span><span>D</span><span>B</span></h1>
  <p class="tagline tagline-top">Pause Your Day</p>
  <p class="tagline tagline-bottom"><span class="soft">And</span> Browse</p>

  <div class="date-band">Monday, October 23, 2017</div>

  <div class="partner partner-guild">
    <span class="mark"></span>
    <span class="name">CSG</span>
  </div>
  <div class="partner partner-union">
    <span class="mark"></span>
    <span class="name">KWNU</span>
  </div>
</main>
</body>
</html>
```